Financial Advisor Resource Firm needs business card design

Need business card design for company in Omaha NE called Tallowbrook Partners. We provide resources to financial advisors....workshop programs, retirement analysis, and insurance planning. I would like to see designs that use grays, greens, black, and white colors. The final design should communicate 'collaboration' and be simple yet attractive to financial planning clients. I will attached our logo and another picture of a puzzle piece coming together. I would like the incorporate the puzzle picture somehow, maybe on the back somehow, with color or just the gray scale....OR, the picture be the front of the card with 'Tallowbrook' definition on it (see upload) and then company logo, employee name, title, address on the back (see ppt uploaded). The following disclosure needs to be included somewhere- Advisory services offered through Marlowe Ridge Advisors, LLC.
Updates

I uploaded a svg and ai file of the logo

Target Market(s)

Financial planning clients and financial advisors....so pretty diverse age range of about 40-70.

Industry/Entity Type

Financial Planning

Contact Information for Business Card

Dennis K. Holloway, MBA
Founder/President
5727 E. Larkspur Avenue
Suite 418
Omaha, NE 68297
Phone- (402) 555-0147
Cell- (402) 555-0183
Fax- (402) 555-0129
email- dennis@tallowbrookgroup.example
web address- www.tallowbrookgroup.example

Colors
1b1b1b
474747
d3d3d3
ffffff
9bcb3c
abd036

Requirements
Must have
• Must include logo provided, must be 2 sided, and must have disclosure...all of these items listed in project description

```html
<!DOCTYPE html>
<html lang="en">
<head>
<meta charset="utf-8">
<title>Tallowbrook Partners – Business Card</title>
<link rel="stylesheet" href="https://fonts.googleapis.com/css2?family=Cinzel:wght@400;600&family=Arimo:wght@400;700&display=swap">
<style>
  :root {
    --ink: #1b1b1b;
    --graphite: #474747;
    --mist: #d3d3d3;
    --paper: #ffffff;
    --leaf: #9bcb3c;
    --lime: #abd036;
    --stage: #2f2f2f;
  }
  * { box-sizing: border-box; margin: 0; padding: 0; }
  html, body { width: 1200px; height: 907px; overflow: hidden; }
  body {
    background: var(--stage);
    display: flex;
    flex-direction: column;
    align-items: center;
    justify-content: center;
    gap: 60px;
    font-family: "Arimo", Arial, sans-serif;
  }
  .card {
    position: relative;
    width: 600px;
    height: 343px;
    border-radius: 22px;
    overflow: hidden;
    box-shadow: 0 12px 30px rgba(0,0,0,.45);
  }

  /* Front */
  .card-front { background: var(--ink); color: var(--paper); }
  .front-photo {
    position: absolute; inset: 0;
    background:
      radial-gradient(ellipse at 70% 55%, #6a6a6a 0%, #3c3c3c 40%, transparent 75%),
      linear-gradient(120deg, #5a5a5a 0%, #2c2c2c 45%, #1b1b1b 100%);
  }
  .definition {
    position: absolute; left: 0; right: 0; top: 86px;
    text-align: center;
  }
  .definition-word {
    font-family: "Cinzel", Georgia, serif;
    font-weight: 400;
    font-size: 58px;
    letter-spacing: 2px;
    color: var(--leaf);
    line-height: 1;
  }
  .definition-phonetic {
    font-family: "Cinzel", Georgia, serif;
    font-size: 20px;
    letter-spacing: 3px;
    margin-top: 14px;
  }
  .definition-meaning {
    font-size: 15px;
    margin-top: 12px;
    letter-spacing: .3px;
  }

  /* Back */
  .card-back { background: var(--paper); color: var(--ink); }
  .brand {
    position: absolute; top: 66px; right: 40px;
    display: flex; align-items: center; gap: 10px;
    white-space: nowrap;
  }
  .brand-dot { width: 14px; height: 14px; border-radius: 50%; background: var(--leaf); flex: none; }
  .brand-name {
    font-family: "Cinzel", Georgia, serif;
    font-weight: 600;
    font-size: 24px;
    line-height: 1;
    color: var(--ink);
    letter-spacing: 1px;
  }
  .person { position: absolute; left: 38px; top: 150px; white-space: nowrap; }
  .person-name {
    font-family: "Cinzel", Georgia, serif;
    font-weight: 600;
    font-size: 19px;
    letter-spacing: 1px;
  }
  .person-title {
    font-weight: 700;
    font-size: 13px;
    color: var(--leaf);
    letter-spacing: .5px;
    margin-top: 2px;
  }
  .address {
    position: absolute; right: 40px; top: 172px;
    text-align: right;
    font-style: normal;
    font-size: 15px;
    line-height: 1.35;
    color: var(--ink);
  }
  .disclosure {
    position: absolute; right: 40px; bottom: 30px;
    width: 220px;
    text-align: right;
    font-size: 10px;
    line-height: 1.4;
    color: var(--graphite);
  }
  .contacts {
    position: absolute; left: 38px; bottom: 30px;
    list-style: none;
    font-size: 15px;
    line-height: 22px;
    white-space: nowrap;
  }
  .contacts li { display: flex; align-items: center; gap: 12px; }
  .contacts svg { width: 14px; height: 14px; fill: var(--leaf); flex: none; }
</style>
</head>
<body>

<section class="card card-front">
  <div class="front-photo" role="img" aria-label="Grayscale photograph of hands fitting puzzle pieces together"></div>
  <div class="definition">
    <p class="definition-word">TALLOW BROOK</p>
    <p class="definition-phonetic">TAL'Ō·BRŎŎK</p>
    <p class="definition-meaning">to come together and unite in common interest and focus</p>
  </div>
</section>

<section class="card card-back">
  <div class="brand">
    <span class="brand-dot"></span>
    <span class="brand-name">Tallowbrook Partners</span>
  </div>

  <div class="person">
    <p class="person-name">DENNIS K. HOLLOWAY, MBA</p>
    <p class="person-title">FOUNDER/PRESIDENT</p>
  </div>

  <address class="address">
    5727 E. Larkspur Avenue<br>
    Suite 418, Omaha, NE 68297
  </address>

  <p class="disclosure">Advisory services offered through Marlowe Ridge Advisors, LLC.</p>

  <ul class="contacts">
    <li>
      <svg viewBox="0 0 16 16" aria-hidden="true"><path d="M3 1l3 3-1.5 2a9 9 0 0 0 5.5 5.5L12 10l3 3-2 2C7 15 1 9 1 3z"/></svg>
      (402) 555-0147
    </li>
    <li>
      <svg viewBox="0 0 16 16" aria-hidden="true"><path d="M4 0h8a1 1 0 0 1 1 1v14a1 1 0 0 1-1 1H4a1 1 0 0 1-1-1V1a1 1 0 0 1 1-1zm1 2v10h6V2zm3 11a1 1 0 1 0 0 2 1 1 0 0 0 0-2z"/></svg>
      (402) 555-0183
    </li>
    <li>
      <svg viewBox="0 0 16 16" aria-hidden="true"><path d="M4 1h8v4H4zM1 6h14v6h-3v3H4v-3H1zm4 5v3h6v-3z"/></svg>
      (402) 555-0129
    </li>
    <li>
      <svg viewBox="0 0 16 16" aria-hidden="true"><path d="M0 3h16v10H0zm1.5 1.2L8 9l6.5-4.8V3.5L8 8 1.5 3.5z"/></svg>
      dennis@tallowbrookgroup.example
    </li>
    <li>
      <svg viewBox="0 0 16 16" aria-hidden="true"><path d="M8 0a8 8 0 1 0 0 16A8 8 0 0 0 8 0zm-1 1.6V5H4a6.5 6.5 0 0 1 3-3.4zm2 0A6.5 6.5 0 0 1 12 5H9zM1.6 7H7v2H1.6a6.5 6.5 0 0 1 0-2zM9 7h5.4a6.5 6.5 0 0 1 0 2H9zm-5 4h3v3.4A6.5 6.5 0 0 1 4 11zm5 0h3a6.5 6.5 0 0 1-3 3.4z"/></svg>
      www.tallowbrookgroup.example
    </li>
  </ul>
</section>

</body>
</html>
```